Website development

Looking for a simple website, containing circa 10-15 pages of brochure-ware content for our new Cafe and Farm Shop venture.

We have a logo, designed through this site, which we think is really strong.

The Cafe and Farm Shop are all about locally sourced, high quality food served in a stunning rural location by happy, friendly staff. Great quality food and drink at sensible prices.

Initially the website needs to contain 10 or so pages of content, which ideally we would like to manage on-going (perhaps not every page, but as many pages as the budget will allow). We want to make sure that the website stays fresh and current and so we want a basic CMS to keep the text areas updated.

We would also like a simple data capture page, so that we can start to generate a database of email addresses for our on-going marketing efforts. Any thoughts around a basic CRM tool gratefully received.

The creative brief can take some inspiration from the logo, but should be bright, clean, welcoming and engaging. Not too over-bearing with colours or content. Fun, easy and interesting to use with all the text and image information clearly displayed.

We don't currently have any imagery beyond the logo, and would like to use as much free stock photography and imagery as possible. If needs be we can take some good quality pictures and provide them.

We're in the process of purchasing the URL(s) at present and will supply them in due course, but they will be based around the trading name.

If you have any more questions please do not hesitate to contact me.

Many thanks
Owen

Industry/Entity Type

Cafe

```html
<!DOCTYPE html>
<html lang="en">
<head>
<meta charset="utf-8">
<title>The Willow Barn Cafe and Farm Shop</title>
<link rel="stylesheet" href="https://fonts.googleapis.com/css2?family=Open+Sans:wght@400;600&display=swap">
<style>
:root{
  --red:#b5321c;
  --rust:#8a3a22;
  --nav-dark:#1f1f1f;
  --green:#3f9a5a;
  --sage:#5fa77a;
  --teal-dark:#3a6b6a;
  --brand:#2a7d6e;
  --text:#2b2b2b;
  --rule:#e3e3e3;
  --footer:#5b5b5b;
  --footer-deep:#474747;
  --white:#ffffff;
}
*{box-sizing:border-box;margin:0;padding:0}
html,body{width:1200px;height:988px;overflow:hidden;background:var(--white)}
body{position:relative;font-family:"Open Sans",Arial,sans-serif;color:var(--text)}
.abs{position:absolute}

.hero{left:0;top:0;width:1200px;height:348px;
  background:
    linear-gradient(90deg,rgba(236,236,232,.85) 0%,rgba(236,236,232,.55) 14%,rgba(236,236,232,0) 26%),
    linear-gradient(180deg,#d9d3c6 0%,#c9cbb8 22%,#a9b39c 36%,#d9b585 52%,#e3bf8b 68%,#c99660 100%)}
.hero-shade{left:0;top:0;width:1200px;height:112px;background:rgba(255,255,255,.4)}
.hero-arrow{width:28px;height:28px;top:219px}
.hero-arrow.prev{left:8px}.hero-arrow.next{left:1164px}

.logo-panel{left:177px;top:0;width:231px;height:165px}
.logo-name{left:186px;top:50px;width:213px;text-align:center;font-size:26px;line-height:30px;font-weight:600;color:var(--brand)}
.logo-sub{left:186px;top:108px;width:213px;text-align:center;font-size:12px;letter-spacing:3px;font-weight:600;color:var(--brand)}

.util-nav{left:598px;top:23px;font-size:11px;letter-spacing:.6px;color:#222;white-space:nowrap}
.util-nav span{margin:0 4px}
.social{top:16px;width:28px;height:28px;border-radius:5px;background:linear-gradient(180deg,#4a4a4a,#262626);border:1px solid #1a1a1a}

.main-nav{left:420px;top:61px;height:28px;display:flex;gap:3px}
.main-nav a{display:block;height:28px;line-height:29px;padding:0 15px;background:var(--nav-dark);color:var(--white);text-decoration:none;font-size:14px;letter-spacing:1.4px}
.main-nav a.active{background:var(--red)}

.welcome-band{left:177px;top:362px;width:844px;height:28px;background:#ececec}
.welcome-title{left:177px;top:362px;width:442px;height:28px;background:var(--sage);border-left:10px solid var(--green);color:var(--white);font-size:16.5px;line-height:28px;padding-left:14px;letter-spacing:.3px;font-weight:400}
.intro{left:179px;top:398px;width:846px;font-size:11px;line-height:15.6px;letter-spacing:.15px}

.rule{left:0;width:1200px;height:2px;background:var(--rule)}

.dish{top:500px;width:202px;height:175px;border:1px solid #ddd;padding:4px}
.dish .photo{height:133px}
.dish .label{margin-top:3px;height:30px;background:var(--rust);color:var(--white);text-align:center;font-size:14px;line-height:31px;letter-spacing:.8px}

.venue{top:699px;width:258px;height:216px;border:1px solid #ddd;padding:4px}
.venue .photo{height:100px}
.venue p{margin:8px 0 0 4px;font-size:10px;line-height:15.6px;letter-spacing:.2px;height:70px;text-align:justify}
.venue .actions{display:flex;height:26px;margin-top:4px}
.venue .name{flex:1;background:var(--sage);color:var(--white);text-align:center;font-weight:600;font-size:12.5px;line-height:27px;letter-spacing:.6px}
.venue .more{width:77px;background:var(--teal-dark);color:var(--white);text-align:center;font-weight:600;font-size:9.5px;line-height:27px;letter-spacing:.4px}

.footer-nav{left:0;top:928px;width:1200px;height:27px;background:var(--footer);color:var(--white);font-size:10px;letter-spacing:.5px;text-align:center;line-height:27px}
.footer-nav span{margin:0 7px}
.copyright{left:0;top:955px;width:1200px;height:33px;background:var(--footer-deep);color:var(--white);font-size:10px;letter-spacing:.4px;text-align:center;line-height:36px}
</style>
</head>
<body>

<div class="abs hero" role="img" aria-label="Bright cafe interior with light wooden tables and chairs, sage green walls and shelves of farm shop jars"></div>
<div class="abs hero-shade"></div>
<svg class="abs hero-arrow prev" viewBox="0 0 28 28"><circle cx="14" cy="14" r="14" fill="#c4262e"/><path d="M16.5 8 10 14l6.5 6" fill="none" stroke="#fff" stroke-width="3"/></svg>
<svg class="abs hero-arrow next" viewBox="0 0 28 28"><circle cx="14" cy="14" r="14" fill="#c4262e"/><path d="M11.5 8 18 14l-6.5 6" fill="none" stroke="#fff" stroke-width="3"/></svg>

<svg class="abs logo-panel" viewBox="0 0 231 165"><polygon points="0,0 231,0 231,165 115,140 0,165" fill="#fff"/></svg>
<div class="abs logo-name">The Willow Barn</div>
<div class="abs logo-sub">CAFE AND FARM SHOP</div>

<div class="abs util-nav">HOME <span>|</span> MY ACCOUNT <span>|</span> NEWSLETTER <span>|</span> SITE MAP</div>
<div class="abs social" style="left:917px" aria-label="Social link"></div>
<div class="abs social" style="left:953px" aria-label="Social link"></div>
<div class="abs social" style="left:988px" aria-label="Social link"></div>

<nav class="abs main-nav">
  <a class="active" href="#">HOME</a>
  <a href="#">RESTAURANT</a>
  <a href="#">HOTEL</a>
  <a href="#">LUNCH</a>
  <a href="#">COFFEE</a>
  <a href="#">CONTACT</a>
</nav>

<div class="abs rule" style="top:348px"></div>
<div class="abs welcome-band"></div>
<h1 class="abs welcome-title">Welcome to The Willow Barn Cafe And Farm Shop</h1>
<div class="abs intro">
  <p>Lorem Ipsum is simply dummy text of the printing and typesetting industry. Lorem Ipsum has been the industry's standard dummy text ever since the 1500s, when an unknown printer took a galley of type and scrambled it to make a type specimen book. It has survived not only five centuries, but also the leap into electronic typesetting, remaining essentially unchanged.</p>
  <p>It was popularised in the 1960s with the release of Letterline sheets containing Lorem Ipsum passages, and more recently with desktop publishing software like Pagecraft Studio including versions of Lorem Ipsum.</p>
</div>

<div class="abs rule" style="top:486px"></div>

<div class="abs dish" style="left:180px"><div class="photo" role="img" aria-label="Breakfast spread with juice, eggs, fruit and pastries" style="background:linear-gradient(170deg,#7a4a24 0%,#c9863a 35%,#e8c68a 60%,#b8542a 100%)"></div><div class="label">BREAKFAST</div></div>
<div class="abs dish" style="left:393px"><div class="photo" role="img" aria-label="Lunch plate with curry, rice, naan and salad" style="background:linear-gradient(160deg,#d9a050 0%,#efe3c4 45%,#e8e4da 60%,#7da447 100%)"></div><div class="label">LUNCH</div></div>
<div class="abs dish" style="left:605px"><div class="photo" role="img" aria-label="Bakery counter with eclairs and cakes" style="background:linear-gradient(170deg,#e9e1d6 0%,#b98f6e 40%,#7a4d34 70%,#4a2e22 100%)"></div><div class="label">BAKERY</div></div>
<div class="abs dish" style="left:817px"><div class="photo" role="img" aria-label="Cup of coffee on a saucer with coffee beans" style="background:radial-gradient(ellipse at 42% 42%,#3a2418 0%,#3a2418 16%,#f4f2ef 24%,#e6e2dc 52%,#8a5a3a 78%,#4a2a1a 100%)"></div><div class="label">COFFEE</div></div>

<div class="abs rule" style="top:685px"></div>

<div class="abs venue" style="left:180px">
  <div class="photo" role="img" aria-label="Cafe dining hall with long tables, diners and pendant lights" style="background:linear-gradient(180deg,#4a2814 0%,#c98a4a 30%,#e8d2a8 55%,#3a2418 100%)"></div>
  <p>It was popularised in the 1960s with the release of Letterline sheets containing top publishing soft-ware like Pagecraft Studio including versions of Lorem Ipsum.</p>
  <div class="actions"><div class="name">CAFE</div><div class="more">READ MORE</div></div>
</div>
<div class="abs venue" style="left:471px">
  <div class="photo" role="img" aria-label="Restaurant room with chandeliers and red table settings" style="background:linear-gradient(180deg,#9a5a28 0%,#e4b56e 40%,#f0dcb0 60%,#b0302a 100%)"></div>
  <p>It was popularised in the 1960s with the release of Letterline sheets containing top publishing soft-ware like Pagecraft Studio including versions of Lorem Ipsum.</p>
  <div class="actions"><div class="name">RESTAURANT</div><div class="more">READ MORE</div></div>
</div>
<div class="abs venue" style="left:759px">
  <div class="photo" role="img" aria-label="Hotel bedroom with striped bedspread, desk and window" style="background:linear-gradient(110deg,#6a4a30 0%,#cdb594 40%,#e8d8c0 55%,#c0703e 80%,#9a3a2a 100%)"></div>
  <p>It was popularised in the 1960s with the release of Letterline sheets containing top publishing soft-ware like Pagecraft Studio including versions of Lorem Ipsum.</p>
  <div class="actions"><div class="name">HOTEL</div><div class="more">READ MORE</div></div>
</div>

<div class="abs footer-nav">HOME <span>|</span> RESTAURANT <span>|</span> ABOUT US <span>|</span> HOTEL <span>|</span> COFFEE <span>|</span> LUNCH <span>|</span> PRIVACY POLICY <span>|</span> TERMS &amp; CONDITION</div>
<div class="abs copyright">© Copyright 2013 By The Willow Barn Cafe and Farm Shop, All rights are Reserved</div>

</body>
</html>
```